GUARANTEED WordPress design needed for a sassy, confident charisma coach!

We need a website design for Mira Haskett's brand new, responsive, Wordpress website.
Mira is a trainer / coach who teaches people how to be more charismatic and runs events, publishes video courses and has an ongoing video blog. Her old website is here: www.mirahaskett-example.co.uk ... but it's now time to have a much better site!
We have a strong idea about the technical components of the website, but we need a designer's eye to create a great style for the site (and provide layered PSD files which our developers will then convert to HTML and CSS).
Mira's brand is sassy, brave, warm and confident. The videos on her existing site give quite a good feel for her personality. We need a clean, stylish and compelling page that isn't too corporate and captures her personality. Every element needs to feel coherent, from fonts and headings to colours and spacing.
The following sites are not exactly what Mira wants (and certainly aren't right in terms of colours) but they give you an idea of the kind of people she is competing against and the area she is operating in:
http://www.fenna-troske.example/
http://brynwellow.example/
Ideally, you will have done something similar and be able to key in on exactly the kind of thing we want: we're not looking to reinvent the wheel. Hopefully you won't mind tweaking a few things if you are close to what we need.
More detail is provided in the word document attached. But in a nutshell we need: a banner, footer, sign-up strap, menu bar, signature and 4 different basic page types. We want bursts of bright colours, contrasted with black and white if possible - sorry we can't be more specific than that...
The word doc also contains some amateur mock-ups as well (the images are also just mockups at this stage) - but although these give a general sense of the structure what we are looking for, we are clearly not designers...so please help! We need a designer's touch!
Kind regards,
Tomas
PS The layered PSD versions of the mockup files are available on Quellbox: https://files.quellbox.example/sh/k27rpw4m1xqzv/QWxnEr8tLpVu3YcMd0aHs?dl=0
Project Deadline Extended Reason: We are looking for a polished, "designed" look. The mock-up that we have provided is just indicative of the features we want. Added Saturday, May 14, 2016
Entrepreneurs who need to sell themselves.
4 page

```html
<!DOCTYPE html>
<html lang="en">
<head>
<meta charset="utf-8">
<title>Mira Haskett — Attract, Connect, Influence</title>
<link rel="stylesheet" href="https://fonts.googleapis.com/css2?family=Fredoka:wght@500;600&family=Raleway:wght@400;500;600;700;800&display=swap">
<style>
:root{
  --magenta:#e8198b;
  --magenta-dark:#c8107a;
  --green:#7ac943;
  --red:#e8252b;
  --blush:#fbe7f1;
  --cyan:#5ccff0;
  --ink:#1d1d1d;
  --grey:#6d6d6d;
  --rule:#e4e4e4;
  --page:#f3f3f3;
  --white:#ffffff;
}
*{box-sizing:border-box;margin:0;padding:0}
html,body{width:1200px;height:4356px;overflow:hidden}
body{font-family:"Raleway",sans-serif;color:var(--ink);background:var(--white)}

/* header */
.site-header{height:100px;display:flex;align-items:center;justify-content:space-between;padding:0 80px;background:var(--white)}
.brand{display:flex;align-items:center;gap:12px;font-family:"Raleway",sans-serif;font-weight:700;font-size:26px;color:var(--magenta)}
.brand-dot{width:14px;height:14px;border-radius:50%;background:var(--magenta)}
.main-nav{display:flex;gap:30px;font-size:14px;font-weight:600;letter-spacing:.5px}
.main-nav a{color:var(--grey);text-decoration:none}
.main-nav a.active{color:var(--magenta)}

/* hero */
.hero{position:relative;height:480px;background:var(--blush);overflow:hidden}
.hero-title{position:absolute;left:80px;top:50px;font-family:"Fredoka",sans-serif;font-weight:600;font-size:116px;line-height:118px;letter-spacing:2px}
.hero-title span{display:block}
.t-green{color:var(--green)}.t-red{color:var(--red)}.t-magenta{color:var(--magenta)}
.hero-portrait{position:absolute;right:60px;top:0;width:420px;height:480px;background:radial-gradient(ellipse at 50% 40%,#d9a58f 0%,#8a3b3b 45%,#c9153a 75%,#f3c6da 100%)}

/* optin band */
.optin{height:260px;background:var(--magenta);position:relative}
.optin-laptop{position:absolute;left:220px;top:16px;width:280px;height:228px;background:linear-gradient(180deg,#4a4a4a 0%,#d9d9d9 70%,#bfbfbf 100%);border-radius:6px}
.optin-copy{position:absolute;left:520px;top:40px;width:600px;color:var(--white);font-size:26px;line-height:34px;font-weight:500}
.signup-form{display:flex;gap:12px;margin-top:22px}
.field{width:190px;height:42px;background:var(--white);border:none;font:500 13px "Raleway",sans-serif;color:#999;padding:0 12px;display:flex;align-items:center}
.btn-green{height:42px;padding:0 26px;background:var(--green);color:var(--white);font:700 14px "Raleway",sans-serif;display:flex;align-items:center;letter-spacing:.5px}
.optin-note{font-size:12px;line-height:16px;margin-top:10px;color:#ffd6ec;font-weight:500}

/* content */
.content{height:3120px;background:var(--page);display:flex;gap:40px;padding:60px 80px 0;overflow:hidden}
.posts{width:680px}
.post{background:var(--white);padding:28px;margin-bottom:56px;box-shadow:0 1px 3px rgba(0,0,0,.12)}
.post-title{font-size:22px;font-weight:700;text-transform:uppercase;letter-spacing:.3px;margin-bottom:18px}
.post-banner{position:relative;height:320px;overflow:hidden;display:flex;align-items:center;padding-left:34px}
.post-banner.short{height:230px}
.banner-text{position:relative;z-index:1;width:390px;font-family:"Raleway",sans-serif;font-weight:600;text-transform:uppercase;line-height:1.12}
.banner-person{position:absolute;right:0;top:0;width:230px;height:100%}
.post-body{margin-top:22px;font-size:14px;line-height:23px;color:var(--grey)}
.post-body p+p{margin-top:14px}
.post-body .more{color:var(--magenta);font-weight:600}
.post-meta{display:flex;gap:30px;border-top:1px solid var(--rule);margin-top:24px;padding-top:20px;font-size:12px;font-weight:700;letter-spacing:.4px}
.post-meta span{display:flex;align-items:center;gap:8px}
.post-meta svg{width:16px;height:16px}

.pagination{display:flex;justify-content:center;gap:10px;margin-top:-10px}
.pagination span{width:34px;height:34px;border-radius:50%;border:2px solid #bbb;display:flex;align-items:center;justify-content:center;font-size:13px;font-weight:600;color:#888}
.pagination span.current{background:#888;color:var(--white);border-color:#888}

/* sidebar */
.sidebar{width:320px}
.widget{background:var(--white);margin-bottom:60px;box-shadow:0 1px 3px rgba(0,0,0,.12)}
.widget-head{height:52px;display:flex;align-items:center;padding:0 20px;color:var(--white);font-size:22px;font-weight:800;letter-spacing:.5px}
.head-red{background:var(--red)}.head-green{background:var(--green)}.head-magenta{background:var(--magenta)}
.recent{list-style:none;padding:10px 20px 14px}
.recent li{padding:14px 0;border-bottom:1px solid var(--rule);font-size:14px;line-height:20px;font-weight:500}
.recent li:last-child{border-bottom:none}
.recent .date{display:flex;align-items:center;gap:8px;font-size:11px;color:#999;margin-top:6px}
.tags{display:flex;flex-wrap:wrap;gap:10px;padding:22px 20px}
.tag{padding:7px 14px;border-radius:16px;color:var(--white);font-size:13px;font-weight:600}
.tag.m{background:var(--magenta)}.tag.r{background:var(--red)}.tag.g{background:var(--green)}
.event{position:relative;height:430px;background:linear-gradient(180deg,#3a3a3a 0%,#171717 45%,#8b1551 100%);margin:0}
.event-copy{position:absolute;left:0;right:0;bottom:26px;text-align:center;color:var(--white)}
.event-copy h3{font-size:28px;line-height:32px;font-weight:800}
.event-copy h3 em{font-style:normal;color:var(--magenta)}
.event-buttons{display:flex;gap:10px;justify-content:center;margin-top:14px}
.event-buttons span{padding:9px 18px;font-size:12px;font-weight:700;border:2px solid var(--white)}
.event-buttons .solid{background:var(--ink);border-color:var(--ink)}
.event-note{font-size:11px;margin-top:10px;color:#ddd}

/* footer */
.newsletter{height:300px;background:var(--magenta);text-align:center;color:var(--white);padding-top:46px}
.newsletter p{font-size:28px;line-height:38px;font-weight:500;width:900px;margin:0 auto}
.newsletter .signup-form{justify-content:center;margin-top:30px}
.newsletter .sad{display:flex;justify-content:center;align-items:center;gap:10px;font-size:16px;margin-top:22px}
.sad i{width:26px;height:26px;border-radius:50%;background:#f8d12f;display:inline-block}
.legal{height:96px;background:#161616;color:#bbb;display:flex;align-items:center;justify-content:space-between;padding:0 80px;font-size:12px;font-weight:500}
.legal-links{display:flex;gap:34px;margin-left:auto;margin-right:40px}
.social{display:flex;gap:8px}
.social i{width:26px;height:26px;background:#3b5f9a;display:block}
.social i:nth-child(2){background:#4aa3df}.social i:nth-child(3){background:#2f77b1}.social i:nth-child(4){background:#c4302b}
</style>
</head>
<body>

<header class="site-header">
  <div class="brand"><span>Mira Haskett</span><span class="brand-dot"></span></div>
  <nav class="main-nav">
    <a class="active" href="#">HOME</a><a href="#">ABOUT US</a><a href="#">CORPORATE</a><a href="#">WORK WITH ME</a><a href="#">EVENTS</a><a href="#">CONTACT</a>
  </nav>
</header>

<section class="hero">
  <h1 class="hero-title"><span class="t-green">ATTRACT</span><span class="t-red">CONNECT</span><span class="t-magenta">INFLUENCE</span></h1>
  <div class="hero-portrait" role="img" aria-label="Portrait of Mira smiling, dark curly hair, red top"></div>
</section>

<section class="optin">
  <div class="optin-laptop" role="img" aria-label="Laptop showing Mira's free video training"></div>
  <div class="optin-copy">
    Learn how to "unlock the superpower" of your charisma and win all the business you want with this FREE training
    <div class="signup-form"><span class="field">First Name</span><span class="field">Email Address</span><span class="btn-green">SIGN ME UP</span></div>
    <div class="optin-note">*I promise not to pass your details on to anyone</div>
  </div>
</section>

<main class="content">
  <div class="posts">

    <article class="post">
      <h2 class="post-title">Public speaking...made easy</h2>
      <div class="post-banner short" style="background:linear-gradient(90deg,#e8254e,#f25a86)">
        <div class="banner-text" style="font-size:54px;color:var(--green);font-weight:500">Public<br>speaking...</div>
        <div class="banner-person" role="img" aria-label="Mira speaking on stage" style="background:linear-gradient(180deg,#f47aa0,#7a2f3f)"></div>
      </div>
      <div class="post-body">
        <p>Lorem ipsum dolor sit amet, consectetur adipiscing elit. Praesent fringilla tortor et mi convallis, ut scelerisque dui rhoncus. Donec quis lorem malesuada, molestie metus et, vehicula ipsum. Pellentesque ultrices venenatis diam rutrum tempor. Sed metus ligula, pharetra ut eros eu, fermentum auctor auctor arcu. Lorem ipsum dolor sit amet, consectetur adipiscing elit.</p>
        <p>Etiam quam mi, vestibulum sit amet maximus mattis, porttitor vitae odio. Cras tempus arcu ut risus dignissim ultrices. Sed dapibus varius justo, vel dictum purus faucibus a. Sed ultrices sodales nibh, a maximus urna fermentum ut. <span class="more">Keep Reading</span></p>
      </div>
      <div class="post-meta">
        <span><svg viewBox="0 0 16 16"><path d="M6 10l4-4M5 8l-2 2a2.5 2.5 0 003.5 3.5l2-2M11 8l2-2A2.5 2.5 0 009.5 2.5l-2 2" stroke="#333" stroke-width="1.6" fill="none"/></svg>PERMALINK</span>
        <span><svg viewBox="0 0 16 16"><circle cx="8" cy="8" r="6.5" stroke="#333" stroke-width="1.6" fill="none"/><path d="M8 4v4l3 2" stroke="#333" stroke-width="1.6" fill="none"/></svg>FEB 8, 2013</span>
        <span><svg viewBox="0 0 16 16"><path d="M8 14L2.5 8.5A3.2 3.2 0 018 4a3.2 3.2 0 015.5 4.5z" fill="#333"/></svg>LIKES</span>
        <span><svg viewBox="0 0 16 16"><path d="M3 6h8l-2-2M13 10H5l2 2" stroke="#333" stroke-width="1.6" fill="none"/></svg>REBLOG</span>
        <span><svg viewBox="0 0 16 16"><circle cx="4" cy="8" r="2" fill="#333"/><circle cx="12" cy="4" r="2" fill="#333"/><circle cx="12" cy="12" r="2" fill="#333"/><path d="M4 8l8-4M4 8l8 4" stroke="#333" stroke-width="1.4"/></svg>SHARE</span>
      </div>
    </article>

    <article class="post">
      <h2 class="post-title">How to start every day in the right frame of mind!</h2>
      <div class="post-banner" style="background:#8dc63f">
        <div class="banner-text" style="font-size:36px;color:var(--ink);font-weight:500">How to start<br>everyday in the<br>right frame of mind!<br><span style="color:var(--magenta);font-size:52px;font-weight:600;display:block;margin-top:10px">5 hot tips</span></div>
        <div class="banner-person" role="img" aria-label="Mira in glasses, arms raised" style="background:linear-gradient(180deg,#a6d665,#5a4a3a)"></div>
      </div>
      <div class="post-body">
        <p>Lorem ipsum dolor sit amet, consectetur adipiscing elit. Praesent fringilla tortor et mi convallis, ut scelerisque dui rhoncus. Donec quis lorem malesuada, molestie metus et, vehicula ipsum. Pellentesque ultrices venenatis diam rutrum tempor. Sed metus ligula, pharetra ut eros eu, fermentum auctor auctor arcu. Lorem ipsum dolor sit amet, consectetur adipiscing elit.</p>
        <p>Etiam quam mi, vestibulum sit amet maximus mattis, porttitor vitae odio. Cras tempus arcu ut risus dignissim ultrices. Sed dapibus varius justo, vel dictum purus faucibus a. Sed ultrices sodales nibh, a maximus urna fermentum ut. <span class="more">Keep Reading</span></p>
      </div>
      <div class="post-meta">
        <span><svg viewBox="0 0 16 16"><path d="M6 10l4-4M5 8l-2 2a2.5 2.5 0 003.5 3.5l2-2M11 8l2-2A2.5 2.5 0 009.5 2.5l-2 2" stroke="#333" stroke-width="1.6" fill="none"/></svg>PERMALINK</span>
        <span><svg viewBox="0 0 16 16"><circle cx="8" cy="8" r="6.5" stroke="#333" stroke-width="1.6" fill="none"/><path d="M8 4v4l3 2" stroke="#333" stroke-width="1.6" fill="none"/></svg>FEB 8, 2013</span>
        <span><svg viewBox="0 0 16 16"><path d="M8 14L2.5 8.5A3.2 3.2 0 018 4a3.2 3.2 0 015.5 4.5z" fill="#333"/></svg>LIKES</span>
        <span><svg viewBox="0 0 16 16"><path d="M3 6h8l-2-2M13 10H5l2 2" stroke="#333" stroke-width="1.6" fill="none"/></svg>REBLOG</span>
        <span><svg viewBox="0 0 16 16"><circle cx="4" cy="8" r="2" fill="#333"/><circle cx="12" cy="4" r="2" fill="#333"/><circle cx="12" cy="12" r="2" fill="#333"/><path d="M4 8l8-4M4 8l8 4" stroke="#333" stroke-width="1.4"/></svg>SHARE</span>
      </div>
    </article>

    <article class="post">
      <h2 class="post-title">Take charge of style...boost your confidence</h2>
      <div class="post-banner" style="background:#f06ab0">
        <div class="banner-text" style="font-size:38px;color:var(--ink);font-weight:500">Take charge of your<br><b style="color:var(--white);font-weight:800">style</b>...boost your<br><b style="font-weight:800">confidence</b></div>
        <div class="banner-person" role="img" aria-label="Mira in a styled outfit and hat" style="background:linear-gradient(180deg,#f48ec4,#4b2b2b)"></div>
      </div>
      <div class="post-body">
        <p>Lorem ipsum dolor sit amet, consectetur adipiscing elit. Praesent fringilla tortor et mi convallis, ut scelerisque dui rhoncus. Donec quis lorem malesuada, molestie metus et, vehicula ipsum. Pellentesque ultrices venenatis diam rutrum tempor. Sed metus ligula, pharetra ut eros eu, fermentum auctor auctor arcu. Lorem ipsum dolor sit amet, consectetur adipiscing elit.</p>
        <p>Etiam quam mi, vestibulum sit amet maximus mattis, porttitor vitae odio. Cras tempus arcu ut risus dignissim ultrices. Sed dapibus varius justo, vel dictum purus faucibus a. Sed ultrices sodales nibh, a maximus urna fermentum ut. <span class="more">Keep Reading</span></p>
      </div>
      <div class="post-meta">
        <span><svg viewBox="0 0 16 16"><path d="M6 10l4-4M5 8l-2 2a2.5 2.5 0 003.5 3.5l2-2M11 8l2-2A2.5 2.5 0 009.5 2.5l-2 2" stroke="#333" stroke-width="1.6" fill="none"/></svg>PERMALINK</span>
        <span><svg viewBox="0 0 16 16"><circle cx="8" cy="8" r="6.5" stroke="#333" stroke-width="1.6" fill="none"/><path d="M8 4v4l3 2" stroke="#333" stroke-width="1.6" fill="none"/></svg>FEB 8, 2013</span>
        <span><svg viewBox="0 0 16 16"><path d="M8 14L2.5 8.5A3.2 3.2 0 018 4a3.2 3.2 0 015.5 4.5z" fill="#333"/></svg>LIKES</span>
        <span><svg viewBox="0 0 16 16"><path d="M3 6h8l-2-2M13 10H5l2 2" stroke="#333" stroke-width="1.6" fill="none"/></svg>REBLOG</span>
        <span><svg viewBox="0 0 16 16"><circle cx="4" cy="8" r="2" fill="#333"/><circle cx="12" cy="4" r="2" fill="#333"/><circle cx="12" cy="12" r="2" fill="#333"/><path d="M4 8l8-4M4 8l8 4" stroke="#333" stroke-width="1.4"/></svg>SHARE</span>
      </div>
    </article>

    <article class="post">
      <h2 class="post-title">Unfulfilled? It's time to think about your values...</h2>
      <div class="post-banner" style="background:var(--cyan)">
        <div class="banner-text" style="font-size:40px;color:var(--ink);font-weight:500;text-transform:none">It's <b style="font-weight:800">time to think</b><br>about your values...<span style="display:block;margin-top:14px;background:var(--magenta);color:var(--white);font-size:36px;padding:8px 12px;text-transform:uppercase;width:400px">Do this exercise now!</span></div>
        <div class="banner-person" role="img" aria-label="Mira in a patterned dress" style="background:linear-gradient(180deg,#8fe0f6,#2d2d2d)"></div>
      </div>
      <div class="post-body">
        <p>Lorem ipsum dolor sit amet, consectetur adipiscing elit. Praesent fringilla tortor et mi convallis, ut scelerisque dui rhoncus. Donec quis lorem malesuada, molestie metus et, vehicula ipsum. Pellentesque ultrices venenatis diam rutrum tempor. Sed metus ligula, pharetra ut eros eu, fermentum auctor auctor arcu. Lorem ipsum dolor sit amet, consectetur adipiscing elit.</p>
        <p>Etiam quam mi, vestibulum sit amet maximus mattis, porttitor vitae odio. Cras tempus arcu ut risus dignissim ultrices. Sed dapibus varius justo, vel dictum purus faucibus a. Sed ultrices sodales nibh, a maximus urna fermentum ut. <span class="more">Keep Reading</span></p>
      </div>
      <div class="post-meta">
        <span><svg viewBox="0 0 16 16"><path d="M6 10l4-4M5 8l-2 2a2.5 2.5 0 003.5 3.5l2-2M11 8l2-2A2.5 2.5 0 009.5 2.5l-2 2" stroke="#333" stroke-width="1.6" fill="none"/></svg>PERMALINK</span>
        <span><svg viewBox="0 0 16 16"><circle cx="8" cy="8" r="6.5" stroke="#333" stroke-width="1.6" fill="none"/><path d="M8 4v4l3 2" stroke="#333" stroke-width="1.6" fill="none"/></svg>FEB 8, 2013</span>
        <span><svg viewBox="0 0 16 16"><path d="M8 14L2.5 8.5A3.2 3.2 0 018 4a3.2 3.2 0 015.5 4.5z" fill="#333"/></svg>LIKES</span>
        <span><svg viewBox="0 0 16 16"><path d="M3 6h8l-2-2M13 10H5l2 2" stroke="#333" stroke-width="1.6" fill="none"/></svg>REBLOG</span>
        <span><svg viewBox="0 0 16 16"><circle cx="4" cy="8" r="2" fill="#333"/><circle cx="12" cy="4" r="2" fill="#333"/><circle cx="12" cy="12" r="2" fill="#333"/><path d="M4 8l8-4M4 8l8 4" stroke="#333" stroke-width="1.4"/></svg>SHARE</span>
      </div>
    </article>

    <nav class="pagination"><span>&lsaquo;</span><span class="current">1</span><span>2</span><span>3</span><span>&rsaquo;</span></nav>
  </div>

  <aside class="sidebar">
    <section class="widget">
      <h3 class="widget-head head-red">MIRA SAYS...</h3>
      <ul class="recent">
        <li>Be more dog: 5 lessons we could learn from our best friends<div class="date"><svg width="12" height="12" viewBox="0 0 12 12"><rect x="1" y="2" width="10" height="9" fill="none" stroke="#999"/><path d="M1 5h10" stroke="#999"/></svg>17th July 2015</div></li>
        <li>Are you letting your world beliefs hold you back?<div class="date"><svg width="12" height="12" viewBox="0 0 12 12"><rect x="1" y="2" width="10" height="9" fill="none" stroke="#999"/><path d="M1 5h10" stroke="#999"/></svg>9th July 2015</div></li>
        <li>How I learned to stop worrying and start NETWORKING<div class="date"><svg width="12" height="12" viewBox="0 0 12 12"><rect x="1" y="2" width="10" height="9" fill="none" stroke="#999"/><path d="M1 5h10" stroke="#999"/></svg>2nd July 2015</div></li>
        <li>Bitchy resting face and other strange – but true – problems<div class="date"><svg width="12" height="12" viewBox="0 0 12 12"><rect x="1" y="2" width="10" height="9" fill="none" stroke="#999"/><path d="M1 5h10" stroke="#999"/></svg>19th June 2015</div></li>
        <li>Bitchy resting face and other strange – but true – problems<div class="date"><svg width="12" height="12" viewBox="0 0 12 12"><rect x="1" y="2" width="10" height="9" fill="none" stroke="#999"/><path d="M1 5h10" stroke="#999"/></svg>12th May 2015</div></li>
      </ul>
    </section>

    <section class="widget">
      <h3 class="widget-head head-green">TAGS</h3>
      <div class="tags">
        <span class="tag r">Body Language</span><span class="tag m">Confidence</span>
        <span class="tag m">Corporate Workshops</span><span class="tag g">Influence</span>
        <span class="tag g">Mindset</span><span class="tag m">Tips</span><span class="tag r">Speaker</span>
        <span class="tag r">Presence</span><span class="tag g">Power Pose</span>
        <span class="tag m">Rapport</span><span class="tag g">Presentation</span>
        <span class="tag r">Style</span><span class="tag m">Spring Wear</span><span class="tag r">Warmth</span>
        <span class="tag m">Vision Board</span>
      </div>
    </section>

    <section class="widget">
      <h3 class="widget-head head-magenta">COMING UP!</h3>
      <div class="event" role="img" aria-label="Mira on stage in front of an audience">
        <div class="event-copy">
          <h3>UNLOCK<br>THE <em>SUPERPOWER</em><br>OF CHARISMA</h3>
          <div class="event-buttons"><span class="solid">LIVE SHOW</span><span>LEARN MORE</span></div>
          <div class="event-note">*Only 6 places left</div>
        </div>
      </div>
    </section>
  </aside>
</main>

<footer>
  <section class="newsletter">
    <p>Hey! Don't go without signing up because you'll miss out on exclusive offers, awesome tips, and weekly motivation in my fab newsletter *</p>
    <div class="signup-form"><span class="field">First Name</span><span class="field">Email Address</span><span class="btn-green">SIGN ME UP</span></div>
    <div class="sad">* And that'll make me sad <i></i></div>
  </section>
  <div class="legal">
    <span>© 2015 Mira Haskett Ltd. All Rights Reserved</span>
    <div class="legal-links"><span>PRIVACY POLICY</span><span>TERMS POLICY</span><span>DISCLAIMERS</span></div>
    <div class="social"><i></i><i></i><i></i><i></i></div>
  </div>
</footer>

</body>
</html>
```